Real Estate For Sale Signage

I'm an independent agent in Lismore NSW Australia with high standards and looking for a catching 'For Sale'sign board.
I like classy, elegant, stylish and simple best.
My colours are red, white and black.
I don't have a logo or other font designs I need to stick to. I like the concept of a house or real estate design.
Before I created this project I played around on publisher and created the PDF attached. I'm not sold on it, but I don't mind the way the name has been layed out. Originally I had a white background with black & red font.
Fancy fonts for my name would be nice, but must not be busy.
Updates

Just wanted to advise that I have updated my brief and used the tools available to help get my ideas through.

Thank you for your work and time.

Kind regards
Marella

Industry/Entity Type

Real Estate

Requirements
Must have
• For Sale
Marella Quint Real Estate (must stand out)
0400 517 382 (must stand out)
17 Tallowood Street North Lismore
www.marellaquintrealestate.com.au

```html
<!DOCTYPE html>
<html lang="en">
<head>
<meta charset="utf-8">
<title>For Sale – Marella Quint Real Estate</title>
<link rel="stylesheet" href="https://fonts.googleapis.com/css2?family=Open+Sans:ital,wght@1,800&family=Nunito:wght@800;900&family=Bodoni+Moda:wght@400&family=Chewy&family=Carlito&display=swap">
<style>
  :root {
    --bg-red: #ff0a0a;
    --bg-rose: #e4596c;
    --bg-mauve: #d49fb8;
    --bg-ice: #c9d6f0;
    --sale-red: #ff0000;
    --name-red: #c00000;
    --estate-red: #b30000;
    --link-red: #ff0000;
    --white: #ffffff;
    --cream: #fff8ee;
    --arrow-shadow: rgba(90, 0, 0, 0.35);
  }
  html, body {
    margin: 0;
    padding: 0;
    width: 1200px;
    height: 1200px;
    overflow: hidden;
  }
  .sign {
    position: relative;
    width: 1200px;
    height: 1200px;
    background: linear-gradient(45deg,
      var(--bg-red) 0%,
      var(--bg-rose) 38%,
      var(--bg-mauve) 68%,
      var(--bg-ice) 100%);
    overflow: hidden;
  }
  .sign > * { position: absolute; margin: 0; }

  .arrow {
    top: 150px;
    width: 148px;
    height: 116px;
    filter: drop-shadow(3px 4px 3px var(--arrow-shadow));
  }
  .arrow--left { left: 115px; }
  .arrow--right { left: 917px; }

  .headline {
    left: 0; right: 0;
    top: 140px;
    text-align: center;
    font-family: "Open Sans", sans-serif;
    font-style: italic;
    font-weight: 800;
    font-size: 134px;
    line-height: 1;
    color: var(--sale-red);
    letter-spacing: 2px;
  }

  .lead-in {
    left: 474px;
    top: 330px;
    font-family: "Nunito", sans-serif;
    font-weight: 900;
    font-size: 76px;
    line-height: 1;
    color: var(--white);
  }

  .agent-name {
    left: 118px;
    top: 415px;
    width: 970px;
    text-align: center;
    font-family: "Nunito", sans-serif;
    font-weight: 900;
    font-size: 128px;
    line-height: 1;
    color: var(--name-red);
    letter-spacing: 1px;
  }

  .agency-type {
    left: 528px;
    top: 553px;
    font-family: "Bodoni Moda", serif;
    font-weight: 400;
    font-size: 66px;
    line-height: 1;
    color: var(--estate-red);
    letter-spacing: 1px;
  }

  .phone {
    left: 196px;
    top: 690px;
    font-family: "Chewy", cursive;
    font-size: 80px;
    line-height: 1;
    color: var(--cream);
    transform: skewX(-8deg);
    white-space: pre;
  }
  .phone__label { margin-right: 70px; }

  .website {
    left: 0; right: 0;
    top: 843px;
    text-align: center;
    font-family: "Carlito", sans-serif;
    font-size: 56px;
    line-height: 1;
    color: var(--link-red);
  }

  .address {
    left: 0; right: 0;
    top: 1020px;
    text-align: center;
    font-family: "Carlito", sans-serif;
    font-size: 60px;
    line-height: 1;
    color: var(--cream);
  }
</style>
</head>
<body>
  <main class="sign">
    <svg class="arrow arrow--left" viewBox="0 0 148 116" aria-hidden="true">
      <polygon points="0,32 84,32 84,0 148,58 84,116 84,84 0,84" fill="#ffffff"/>
    </svg>
    <h1 class="headline">For Sale</h1>
    <svg class="arrow arrow--right" viewBox="0 0 148 116" aria-hidden="true">
      <polygon points="148,32 64,32 64,0 0,58 64,116 64,84 148,84" fill="#ffffff"/>
    </svg>

    <p class="lead-in">With</p>
    <p class="agent-name">Marella Quint</p>
    <p class="agency-type">REAL ESTATE</p>

    <p class="phone"><span class="phone__label">CALL</span>0400 517 382</p>

    <p class="website">www.marellaquintrealestate.com.au</p>

    <p class="address">17 Tallowood Street, North Lismore</p>
  </main>
</body>
</html>
```